Stationery design for law/Property/finance business

We need stationery design for a Law/Property/Finance business called Ridgemoor. Logo is attached.
we require a letterhead and with compliments slip.
Would like to see a very simple professional design using the colours of the logo and offset against Charcoal colours. Maybe a charcoal band for header and footer with logo and details appearing in it? Former letterhead attached for examples.
we require the project to be provided in word, pdf and jpeg format.
we require the following details on the stationery:
Cairns Phone: 07 40551926
Weipa Phone: 07 40613847
Mobile: 0491 570 384
Fax: 07 40338172
email: admin@ridgemoorholdings-example.com.au
ABN 51 824 306 917

```html
<!DOCTYPE html>
<html lang="en">
<head>
<meta charset="utf-8">
<title>Ridgemoor Stationery</title>
<link rel="stylesheet" href="https://fonts.googleapis.com/css2?family=Questrial&display=swap">
<style>
  :root{
    --bg:#c9c9cc;
    --paper:#f4f4f4;
    --brand:#4a72b0;
    --ink:#444;
    --ghost:rgba(0,0,0,.045);
    --ghost-light:rgba(255,255,255,.07);
  }
  *{box-sizing:border-box;margin:0;padding:0}
  html,body{width:1200px;height:991px;overflow:hidden}
  body{background:var(--bg);font-family:"Questrial",sans-serif;color:var(--ink);position:relative}
  .piece{position:absolute;background:var(--paper);overflow:hidden}
  .wordmark{font-family:"Questrial",sans-serif;color:var(--brand);letter-spacing:.01em;white-space:nowrap;position:absolute}
  .wordmark.light{color:#fff}
  .ghost-disc{position:absolute;border-radius:50%;background:var(--ghost)}
  .ghost-disc.light{background:var(--ghost-light)}
  .small{font-size:5px;line-height:1.45;position:absolute;white-space:nowrap}
  .accent{color:var(--brand)}

  /* Letterhead */
  .letterhead{left:71px;top:104px;width:398px;height:560px}
  .letterhead .wordmark{right:36px;top:58px;font-size:19px}
  .letterhead .ghost-disc{left:-60px;top:340px;width:320px;height:320px}
  .letterhead .footer{right:36px;bottom:18px;text-align:right}

  /* Folder */
  .folder{left:507px;top:90px;width:432px;height:576px;background:var(--brand);border-radius:4px}
  .folder .spine{position:absolute;left:26px;top:0;bottom:0;width:1px;background:rgba(0,0,0,.08)}
  .folder .wordmark{left:0;right:0;text-align:center;top:98px;font-size:28px}
  .folder .ghost-disc{left:-80px;top:230px;width:380px;height:380px}
  .folder .web{position:absolute;left:0;right:0;bottom:34px;text-align:center;color:#e6ecf5;font-size:8px;letter-spacing:.04em}

  /* Business cards */
  .card-front{left:66px;top:696px;width:171px;height:94px}
  .card-front .wordmark{left:11px;top:12px;font-size:11px}
  .card-front .ghost-disc{left:110px;top:-20px;width:90px;height:90px}
  .card-front .person{position:absolute;left:11px;top:54px}
  .card-front .person .name{font-size:5px;color:var(--brand);font-weight:bold;letter-spacing:.03em}
  .card-front .person .role{font-size:4px}
  .card-front .details{left:11px;top:70px;font-size:4px}
  .card-back{left:66px;top:810px;width:171px;height:95px;background:var(--brand)}
  .card-back .wordmark{left:0;right:0;text-align:center;top:40px;font-size:13px}

  /* Compliments slip */
  .slip{left:266px;top:696px;width:415px;height:209px}
  .slip .wordmark{left:22px;top:52px;font-size:18px}
  .slip .ghost-disc{left:220px;top:30px;width:240px;height:240px}
  .slip .address{left:22px;bottom:14px;font-size:5.5px}

  /* Envelope */
  .envelope{left:718px;top:696px;width:415px;height:209px}
  .envelope .flap{position:absolute;left:0;top:0;width:415px;height:58px}
  .envelope .flap-mark{position:absolute;left:200px;top:23px;width:12px;height:12px;border-radius:50%;background:#fff}
</style>
</head>
<body>

<section class="piece letterhead" aria-label="Letterhead">
  <div class="ghost-disc"></div>
  <div class="wordmark">RIDGEMOOR</div>
  <div class="small footer">
    Unit 5 Harbour Centre - Marina Parade, Tidemere Vic 3999<br>
    <span class="accent">T:</span> 0491 570 384 - <span class="accent">E:</span> info@ridgemoorholdings-example.com.au - www.<span class="accent">ridgemoorholdings-example</span>.com.au
  </div>
</section>

<section class="piece folder" aria-label="Presentation folder">
  <div class="spine"></div>
  <div class="ghost-disc light"></div>
  <div class="wordmark light">RIDGEMOOR</div>
  <div class="web">www.ridgemoorholdings-example.com.au</div>
</section>

<section class="piece card-front" aria-label="Business card front">
  <div class="ghost-disc"></div>
  <div class="wordmark">RIDGEMOOR</div>
  <div class="person">
    <div class="name">JORDAN WHITFIELD</div>
    <div class="role">General Manager</div>
  </div>
  <div class="small details">
    Unit 5 Harbour Centre - Marina Parade, Tidemere Vic 3999<br>
    T: 0491 570 384 - E: info@ridgemoorholdings-example.com.au<br>
    <span class="accent">www.ridgemoorholdings-example.com.au</span>
  </div>
</section>

<section class="piece card-back" aria-label="Business card back">
  <div class="wordmark light">RIDGEMOOR</div>
</section>

<section class="piece slip" aria-label="Compliments slip">
  <div class="ghost-disc"></div>
  <div class="wordmark">RIDGEMOOR</div>
  <div class="small address">
    Unit 5 Harbour Centre<br>
    Marina Parade<br>
    Tidemere Vic 3999
  </div>
</section>

<section class="piece envelope" aria-label="Envelope">
  <svg class="flap" viewBox="0 0 415 58" aria-hidden="true">
    <polygon points="0,0 415,0 399,58 16,58" fill="var(--brand)"/>
  </svg>
  <div class="flap-mark"></div>
</section>

</body>
</html>
```